【依頼の目的/概要】
電子書籍(bookrie)の表紙デザインをお願いします。

【画像サイズ】※BRPより抜粋
表紙ファイルの理想的な寸法は2,560×1,600ピクセルです。
注:画像の寸法は10,000×10,000ピクセルです。

【タイトル】
資格試験 ゴールダッシュ・速習・楽々学習術

サブタイトル
通れる学び方

【著者】
行政書士 社会保険労務士
森川澄江

【本の内容】
行政書士試験の勉強を短期間で仕上げて、合格する勉強法を
書いた本です。

【デザイン要望】
特にこだわりません。
素敵なデザインの応募を楽しみにしています。
※次点、次々点の方への参加報酬を設定しました。

その他
必要な情報がありましたらお問い合わせください。

本を以下に添付します。
本文中にエクセルで作成した表を挿入します。

明るく見やすく、わかり易い表現が良かったです。

皆様お疲れ様でした。
T_okabe様には訂正を速攻して頂きありがとうございました。
最後まで迷いました。
皆様のご依頼が増えますことをご祈念申し上げます。

```html
<!DOCTYPE html>
<html lang="ja">
<head>
<meta charset="UTF-8">
<title>資格試験 ゴールダッシュ・速習・楽々学習術</title>
<link href="https://fonts.googleapis.com/css2?family=Noto+Sans+JP:wght@500;700;900&display=swap" rel="stylesheet">
<style>
  :root {
    --orange: #f7941d;
    --orange-light: #fba02f;
    --white: #ffffff;
    --black: #111111;
    --yellow: #fff200;
  }
  html, body { margin: 0; padding: 0; overflow: hidden; }
  .cover {
    position: relative;
    width: 750px; height: 1200px;
    background: linear-gradient(180deg, var(--orange-light), var(--orange));
    font-family: "Noto Sans JP", sans-serif;
    overflow: hidden;
  }
  .center-panel {
    position: absolute; left: 105px; top: 265px;
    width: 540px; height: 735px;
    background: var(--white);
    border-radius: 24px;
  }
  .subtitle {
    position: absolute; left: 318px; top: 155px;
    width: 432px; height: 95px;
    background: var(--black); color: var(--white);
    border-radius: 10px 0 0 10px;
    display: flex; align-items: center; justify-content: center;
    font-size: 52px; font-weight: 900; letter-spacing: 2px;
  }
  .title {
    position: absolute; left: 0; right: 0; top: 455px;
    text-align: center; margin: 0;
    font-size: 148px; font-weight: 900; color: var(--black);
    line-height: 1; letter-spacing: 4px;
  }
  .tags {
    position: absolute; left: 0; right: 0; top: 643px;
    display: flex; justify-content: center; gap: 14px;
  }
  .tag {
    background: var(--yellow); color: var(--black);
    border: 5px solid var(--black); border-radius: 8px;
    padding: 2px 12px;
    font-size: 46px; font-weight: 900; line-height: 1.3;
  }
  .tagline {
    position: absolute; left: 0; right: 0; top: 738px;
    text-align: center; font-size: 44px; font-weight: 900; color: var(--black);
    line-height: 1.2;
  }
  .author-role {
    position: absolute; left: 0; right: 0; top: 998px;
    text-align: center; color: var(--white);
    font-size: 32px; font-weight: 700; letter-spacing: 2px;
    line-height: 1.2;
  }
  .author-name {
    position: absolute; left: 0; right: 0; top: 1060px;
    text-align: center; color: var(--white);
    font-size: 52px; font-weight: 900; letter-spacing: 4px;
    line-height: 1.2;
  }
</style>
</head>
<body>
<div class="cover">
  <div class="center-panel" role="img" aria-label="白い装飾シルエットの背景"></div>

  <div class="subtitle">通れる学び方</div>

  <h1 class="title">資格試験</h1>
  <div class="tags">
    <span class="tag">ゴールダッシュ</span>
    <span class="tag">速習</span>
    <span class="tag">楽々</span>
  </div>
  <div class="tagline">学習術</div>

  <div class="author-role">行政書士&nbsp;&nbsp;社会保険労務士</div>
  <div class="author-name">森川澄江</div>
</div>
</body>
</html>
```